Mara Lindqvist Advisory Business Cards

Hi - using the information and logo provided I require a two sided business card designed with the following information. The business card is a 'mini card' 3.5" x 1.25".

Front of card should be the logo attached but inverted (so the background is the peach colour and the logo white).

Back should have these details. If we can't fit the Instragram and Facebook part can we just put the little logos.

Mara Lindqvist

Art and Design Consultant
Dealer - Curator - Events - Styling - Creative Sourcing

P: 0438 519 207
E: mara@maralindqvistadvisory.com
W: www.maralindqvistadvisory.com
I (instagram image please): maralindqvistadvisory F (Facebook image please): MaraLindqvistAdvisor

Target Market(s)

Galleries, artists, art buyers, interior design clients, event managers, creative types

Industry/Entity Type

Business

```html
<!DOCTYPE html>
<html lang="en">
<head>
<meta charset="utf-8">
<title>Mara Lindqvist Advisory – Mini Business Cards</title>
<link rel="stylesheet" href="https://fonts.googleapis.com/css2?family=Oswald:wght@300&family=PT+Sans:wght@400;700&display=swap">
<style>
  :root {
    --board-dark: #2b2b2b;
    --board-edge: #4a4a4a;
    --peach: #f8b89a;
    --peach-soft: #f5c8a8;
    --peach-soft-2: #f2c09f;
    --white: #ffffff;
    --ink-grey: #8a8a8a;
    --ink-dark: #5e5e5e;
  }
  * { box-sizing: border-box; margin: 0; padding: 0; }
  html, body { width: 1200px; height: 1000px; overflow: hidden; }
  body {
    position: relative;
    background: linear-gradient(90deg, #6a6a6a 0, var(--board-dark) 55px, var(--board-dark) 1140px, var(--board-edge) 1200px);
    font-family: "PT Sans", sans-serif;
  }
  .board-label {
    position: absolute;
    left: 70px; top: 472px; width: 140px;
    font-family: "Oswald", sans-serif;
    font-weight: 300;
    font-size: 20px;
    line-height: 42px;
    color: var(--white);
    text-align: center;
  }
  .card {
    position: absolute;
    left: 216px; width: 858px;
    border: 3px solid var(--white);
    overflow: hidden;
  }
  .card--front { top: 27px; height: 305px; background: var(--peach); }
  .card--pattern { top: 354px; height: 306px; }
  .card--back { top: 680px; height: 306px; width: 856px; background: var(--white); border: 0; }

  .pattern-fill {
    position: absolute; inset: 0;
    background: radial-gradient(ellipse at 40% 40%, var(--peach-soft) 0, var(--peach-soft-2) 100%);
  }
  .front-mark {
    position: absolute; left: 0; right: 0; top: 118px;
    text-align: center;
    color: var(--white);
    font-weight: 400;
    font-size: 34px;
    letter-spacing: 4px;
  }
  .front-url {
    position: absolute; left: 0; right: 0; bottom: 10px;
    text-align: center;
    color: var(--white);
    font-size: 21px;
  }
  .holder-name {
    position: absolute; left: 0; right: 0; top: 46px;
    text-align: center;
    color: var(--peach);
    font-weight: 700;
    font-size: 27px;
    letter-spacing: 0.5px;
  }
  .services-band {
    position: absolute; left: 0; right: 0; top: 84px; height: 27px;
    background: var(--peach);
    color: var(--white);
    font-weight: 700;
    font-size: 18.5px;
    line-height: 27px;
    text-align: center;
  }
  .contact-list { position: absolute; left: 26px; top: 143px; list-style: none; }
  .contact-list li {
    display: flex; align-items: center;
    height: 36px;
    color: var(--ink-grey);
    font-size: 18.5px;
  }
  .contact-icon { width: 22px; height: 18px; margin-right: 11px; flex: none; }
  .social-square { width: 17px; height: 17px; margin: 0 13px 0 3px; background: var(--peach); border-radius: 3px; flex: none; }
  .brand-block { position: absolute; left: 560px; top: 126px; width: 306px; text-align: center; }
  .brand-dot { display: block; width: 84px; height: 84px; margin: 0 auto 24px; border-radius: 50%; background: var(--peach); }
  .brand-name { color: var(--ink-dark); font-size: 22px; letter-spacing: 3px; line-height: 28px; }
</style>
</head>
<body>

<div class="board-label">PATTERN<br>BACKGROUND</div>

<section class="card card--front">
  <p class="front-mark">MARA LINDQVIST ADVISORY</p>
  <p class="front-url">www.maralindqvistadvisory.com</p>
</section>

<section class="card card--pattern">
  <div class="pattern-fill" role="img" aria-label="Soft peach decorative pattern background"></div>
  <p class="front-mark">MARA LINDQVIST ADVISORY</p>
  <p class="front-url">www.maralindqvistadvisory.com</p>
</section>

<section class="card card--back">
  <h1 class="holder-name">MARA LINDQVIST</h1>
  <p class="services-band">Art and Design Consultant - Dealer - Curator - Events - Styling - Creative Sourcing</p>

  <ul class="contact-list">
    <li>
      <svg class="contact-icon" viewBox="0 0 22 18" aria-hidden="true">
        <path d="M2 6 Q11 0 20 6 L18 8 L15 6 L15 4 Q11 3 7 4 L7 6 L4 8 Z" fill="var(--peach)"/>
        <rect x="5" y="9" width="12" height="8" rx="1.5" fill="var(--peach)"/>
      </svg>
      0438 519 207
    </li>
    <li>
      <svg class="contact-icon" viewBox="0 0 22 18" aria-hidden="true">
        <rect x="1" y="3" width="20" height="13" fill="none" stroke="var(--peach)" stroke-width="2"/>
        <path d="M1 3 L11 11 L21 3" fill="none" stroke="var(--peach)" stroke-width="2"/>
      </svg>
      mara@maralindqvistadvisory.com
    </li>
    <li><span class="social-square" aria-hidden="true"></span>maralindqvistadvisory</li>
    <li><span class="social-square" aria-hidden="true"></span>MaraLindqvistAdvisor</li>
  </ul>

  <div class="brand-block">
    <span class="brand-dot" aria-hidden="true"></span>
    <p class="brand-name">MARA LINDQVIST ADVISORY</p>
  </div>
</section>

</body>
</html>
```